Quarrytide
Quarrytide - Financial Services
Financial Services
www.quarrytidepay.com
Our team has been providing solutions for workers compensation for business owners for over 22 years, our service is provoided at no charge (as it is paid for by the vendor). What makes us unique is our ability to write just about every size company (3 man to 1000) and industry in every state,. Our programs simlyfy the business owners way of doing business by eliminationg several annoying functions that business owners face. For example, with our program a business owner would write one check for payroll, that check would cover his payroll, workers compensation, payroll taxes, employee deductions and garnishments, direct deposit and benefit deductions, year end W-2's and the liabilities that come with year end W-2's. Our program we keeps business owners compliant by keeping them informed about new requirements, labor laws, we provide all employee applications, safety posters, they are able to call with any employee related questions about hiring and firing and so on. All usually for less that they can do it themselves.
Busy, wordy
Service Oriented
White/possible grey, logo colors
Blues and whites and greys, logo colors
left side
We have a content writer completing the text, our home page will contain very little text and focus more as a landing page. The site itself needs to be very clean, simple and easy to navigate but will also allow viewers to go deep into the site if they want to find information, yet at the same time it will not force people away because of too much content

```html
<!DOCTYPE html>
<html lang="en">
<head>
<meta charset="utf-8">
<title>Quarrytide - Financial Services</title>
<link rel="stylesheet" href="https://fonts.googleapis.com/css2?family=Open+Sans:wght@400;600;700&family=PT+Sans:wght@400;700&display=swap">
<style>
  :root {
    --page-top: #c9c9c9;
    --page-mid: #efefef;
    --page-light: #f7f7f7;
    --brand-blue: #1f8fd0;
    --brand-blue-light: #5cc0ee;
    --brand-navy: #1d4f7a;
    --text-dark: #2a2a2a;
    --text-grey: #8a8a8a;
    --text-body: #9a9a9a;
    --nav-top: #9c9c9c;
    --nav-bottom: #6f6f6f;
    --footer-top: #8c8c8c;
    --footer-bottom: #5f5f5f;
    --white: #ffffff;
  }
  * { margin: 0; padding: 0; box-sizing: border-box; }
  html, body { width: 1200px; height: 1000px; overflow: hidden; }
  body {
    position: relative;
    font-family: "Open Sans", Arial, sans-serif;
    background: linear-gradient(to bottom, var(--page-top) 0, var(--page-mid) 150px, var(--page-light) 420px, var(--page-light) 890px);
    color: var(--text-dark);
  }

  /* Header */
  .brand { position: absolute; left: 118px; top: 62px; display: flex; align-items: center; gap: 14px; }
  .brand-mark { width: 86px; height: 86px; border-radius: 50%; background: var(--brand-blue); }
  .brand-name { font-family: "PT Sans", Arial, sans-serif; font-weight: 700; font-size: 46px; color: var(--brand-navy); letter-spacing: 0.5px; }

  .contact { position: absolute; right: 138px; top: 76px; text-align: left; }
  .contact-label { font-family: "PT Sans", Arial, sans-serif; font-size: 25px; color: var(--text-grey); }
  .contact-phone { font-family: "PT Sans", Arial, sans-serif; font-size: 28px; color: var(--brand-blue); letter-spacing: 1px; margin-top: -4px; }

  /* Navigation */
  .main-nav {
    position: absolute; left: 113px; top: 173px; width: 968px; height: 38px;
    background: linear-gradient(to bottom, var(--nav-top), var(--nav-bottom));
    display: flex; align-items: stretch;
    border-bottom: 1px solid #5a5a5a;
  }
  .main-nav a { color: var(--white); text-decoration: none; font-size: 15px; display: flex; align-items: center; justify-content: center; }
  .main-nav .home { width: 90px; background: linear-gradient(to bottom, #d8d8d8, #b2b2b2); color: #555; }
  .main-nav .item { width: 125px; }

  /* Hero */
  .hero {
    position: absolute; left: 113px; top: 227px; width: 968px; height: 332px;
    background: var(--white);
    box-shadow: 0 14px 18px -10px rgba(0,0,0,0.35);
  }
  .hero-visual {
    position: absolute; left: 0; top: 0; width: 563px; height: 332px;
    background: linear-gradient(135deg, #eef4fa 0%, #b9d9f2 45%, #3a97dc 75%, #1c6fb8 100%);
  }
  .hero-copy { position: absolute; left: 592px; top: 110px; }
  .hero-title { font-family: "PT Sans", Arial, sans-serif; font-size: 32px; line-height: 40px; color: #555; font-weight: 400; }
  .hero-sub { font-family: "PT Sans", Arial, sans-serif; font-size: 19px; color: var(--brand-blue); margin-top: 4px; }
  .slider-dots { position: absolute; left: 880px; top: 288px; display: flex; gap: 5px; }
  .slider-dots span { width: 18px; height: 13px; background: #ddd; }
  .slider-dots .active { background: var(--brand-blue-light); }

  /* Feature columns */
  .features { position: absolute; left: 119px; top: 612px; display: flex; gap: 40px; }
  .feature { width: 216px; }
  .feature h2 { font-family: "PT Sans", Arial, sans-serif; font-weight: 400; font-size: 19px; line-height: 20px; color: var(--text-dark); height: 44px; }
  .feature-tag {
    margin-top: 6px; height: 20px;
    background: linear-gradient(to bottom, var(--brand-blue-light), var(--brand-blue));
    color: var(--white); font-size: 10px; line-height: 20px; padding-left: 10px;
  }
  .feature p { margin-top: 20px; font-size: 11px; line-height: 17px; color: var(--text-body); }
  .read-more { display: block; margin-top: 20px; font-size: 11px; font-weight: 700; color: var(--brand-navy); text-decoration: none; }

  /* Footer */
  .site-footer {
    position: absolute; left: 0; top: 890px; width: 1200px; height: 110px;
    background: linear-gradient(to bottom, var(--footer-top), var(--footer-bottom));
  }
  .copyright { position: absolute; left: 135px; top: 22px; font-size: 15px; color: var(--white); }
  .follow { position: absolute; left: 876px; top: 20px; display: flex; align-items: center; gap: 10px; color: var(--white); font-size: 14px; }
  .follow .icon { width: 24px; height: 24px; background: #2c2c2c; border-radius: 3px; }
</style>
</head>
<body>
  <header>
    <div class="brand">
      <span class="brand-mark"></span>
      <span class="brand-name">QUARRYTIDE</span>
    </div>
    <div class="contact">
      <div class="contact-label">Contact Us Now</div>
      <div class="contact-phone">555.014.2290</div>
    </div>
  </header>

  <nav class="main-nav">
    <a class="home" href="#">Home</a>
    <a class="item" href="#">About Us</a>
    <a class="item" href="#">Services</a>
    <a class="item" href="#">Portfolio</a>
    <a class="item" href="#">Contact</a>
  </nav>

  <section class="hero">
    <div class="hero-visual" role="img" aria-label="Blue 3D bar chart with a rising arrow showing financial growth"></div>
    <div class="hero-copy">
      <h1 class="hero-title">WE ARE EXPERTS IN THE<br>FINANCIAL INDUSTRY</h1>
      <div class="hero-sub">SEE WHAT WE CAN DO FOR YOU</div>
    </div>
    <div class="slider-dots"><span class="active"></span><span></span><span></span></div>
  </section>

  <main class="features">
    <article class="feature">
      <h2>EXCELLENT SOLUTION<br>FOR YOUR BUSINESS</h2>
      <div class="feature-tag">Aenean vitae nibh dolor</div>
      <p>Lorem Ipsum is simply dummy text of the printing and typesetting industry. Lorem Ipsum has been the industry's standard dummy text ever since the 1500s, when an unknown printer took a galley of type and scrambled it to make a</p>
      <a class="read-more" href="#">READ MORE »</a>
    </article>
    <article class="feature">
      <h2>TIME SAVING PROGRAM<br>FOR COMPANIES</h2>
      <div class="feature-tag">Nulla porta sed quam</div>
      <p>Lorem Ipsum is simply dummy text of the printing and typesetting industry. Lorem Ipsum has been the industry's standard dummy text ever since the 1500s, when an unknown printer took a galley of type and scrambled it to make a</p>
      <a class="read-more" href="#">READ MORE »</a>
    </article>
    <article class="feature">
      <h2>TESTIMONIALS FROM<br>OUR VALUED CLIENTS</h2>
      <div class="feature-tag">Donec ut metus velit</div>
      <p>Lorem Ipsum is simply dummy text of the printing and typesetting industry. Lorem Ipsum has been the industry's standard dummy text ever since the 1500s, when an unknown printer took a galley of type and scrambled it to make a</p>
      <a class="read-more" href="#">READ MORE »</a>
    </article>
    <article class="feature">
      <h2>LATEST NEWS &amp;<br>EVENTS</h2>
      <div class="feature-tag">Cras eget felis nunc</div>
      <p>Lorem Ipsum is simply dummy text of the printing and typesetting industry. Lorem Ipsum has been the industry's standard dummy text ever since the 1500s, when an unknown printer took a galley of type and scrambled it to make a</p>
      <a class="read-more" href="#">READ MORE »</a>
    </article>
  </main>

  <footer class="site-footer">
    <div class="copyright">© Copyright 2011 Quarrytide Works. All Rights Reserved</div>
    <div class="follow">
      <span>follow us</span>
      <span class="icon"></span>
      <span class="icon"></span>
      <span class="icon"></span>
      <span class="icon"></span>
    </div>
  </footer>
</body>
</html>
```